letterhead design for a investing company*

Design an appealing business letterhead to match with our existing logo and attract new customers. Our customers are mainly corporate managers which are detail oriented and judge the company ability to perform a good service based on small details. A professional letterhead will give a good first impression.

Target Market(s)

New customers and business owners

Industry/Entity Type

Marketplace

Font styles to use
Sans Serif
Script

Requirements
Must have
• Must be a professional and elegant design that attracts interest from people who receives it

```html
<!DOCTYPE html>
<html lang="en">
<head>
<meta charset="utf-8">
<title>Harbor Vale — Stationery</title>
<link rel="stylesheet" href="https://fonts.googleapis.com/css2?family=Open+Sans:wght@400;600;700&family=Roboto:wght@400;500&display=swap">
<style>
  :root {
    --navy: #121c3b;
    --gold: #fdb913;
    --paper: #ffffff;
    --backdrop: #d9d9db;
    --body-text: #5a5a5a;
    --signature-tone: #e6e6e6;
  }
  * { box-sizing: border-box; margin: 0; padding: 0; }
  html, body { width: 1200px; height: 1122px; overflow: hidden; }
  body {
    background: var(--backdrop);
    position: relative;
    font-family: "Open Sans", Arial, sans-serif;
  }
  .back-sheet {
    position: absolute; left: 129px; top: 214px;
    width: 564px; height: 798px; background: var(--navy);
  }
  .letterhead {
    position: absolute; left: 220px; top: 124px;
    width: 565px; height: 800px; background: var(--paper);
  }
  .brand {
    display: flex; align-items: center; gap: 8px;
    font-family: "Open Sans", Arial, sans-serif;
    font-weight: 700; color: var(--navy); letter-spacing: -0.5px;
  }
  .brand-dot { border-radius: 50%; background: var(--gold); flex: none; }
  .letterhead .brand { position: absolute; left: 49px; top: 64px; font-size: 32px; }
  .letterhead .brand-dot { width: 26px; height: 26px; }
  .contact {
    position: absolute; left: 366px; top: 66px;
    list-style: none; font-size: 12.5px; color: var(--navy); line-height: 15.5px;
  }
  .contact li { display: flex; align-items: center; gap: 5px; }
  .contact svg { width: 10px; height: 10px; fill: var(--gold); flex: none; }
  .letter {
    position: absolute; left: 50px; top: 186px; width: 463px;
    font-size: 10.8px; line-height: 15.5px; color: var(--body-text);
    text-align: justify; hyphens: auto;
  }
  .letter p { margin-bottom: 15.5px; }
  .letter .salutation { margin-bottom: 15px; }
  .signature {
    width: 70px; height: 66px; background: var(--signature-tone);
    margin-top: 8px;
  }
  .sender {
    position: absolute; left: 50px; top: 746px;
    font-family: "Roboto", Arial, sans-serif; font-size: 12px;
    line-height: 15px; color: var(--navy);
  }
  .sender strong { font-weight: 500; }
  .footer-band {
    position: absolute; left: 0; bottom: 0; width: 100%; height: 12px; display: flex;
  }
  .footer-band .gold { width: 451px; background: var(--gold); }
  .footer-band .navy { flex: 1; background: var(--navy); margin-left: 3px; }
  .card {
    position: absolute; left: 849px; width: 240px; height: 136px;
    display: flex; align-items: center; justify-content: center;
  }
  .card .brand { font-size: 22px; }
  .card .brand-dot { width: 18px; height: 18px; }
  .card-light { top: 390px; background: var(--paper); }
  .card-dark { top: 588px; background: var(--navy); }
  .card-dark .brand { color: var(--paper); }
</style>
</head>
<body>
  <div class="back-sheet"></div>

  <section class="letterhead">
    <div class="brand"><span class="brand-dot"></span>Harbor Vale</div>

    <ul class="contact">
      <li><svg viewBox="0 0 10 10"><path d="M1 2c0-1 1-1.5 2-1.5l1 2-1 1c.6 1.2 1.4 2 2.5 2.5l1-1 2 1c0 1-.5 2-1.5 2C3.5 8 1 5.5 1 2z"/></svg>555.204.7781</li>
      <li><svg viewBox="0 0 10 10"><path d="M0 2h10v6H0z M0.5 2.5l4.5 3 4.5-3" fill="var(--gold)"/><path d="M0.8 2.6 5 5.4 9.2 2.6" stroke="#fff" stroke-width=".8" fill="none"/></svg>hello@harborvale.com.au</li>
      <li><svg viewBox="0 0 10 10"><circle cx="5" cy="5" r="4.6"/><path d="M.5 5h9M5 .5c-2 2.5-2 6.5 0 9M5 .5c2 2.5 2 6.5 0 9" stroke="#fff" stroke-width=".7" fill="none"/></svg>www.harborvale.com.au</li>
    </ul>

    <div class="letter">
      <p class="salutation">Dear customer,</p>
      <p>Lorem ipsum dolor sit amet, consectetur adipisicing elit, sed do eiusmod tempor incididunt ut labore et dolore magna aliqua. Ut enim ad minim veniam, quis nostrud exercitation ullamco laboris nisi ut aliquip ex ea commodo consequat. Duis aute irure dolor in reprehenderit in voluptate velit esse cillum dolore eu fugiat nulla pariatur. Excepteur sint occaecat cupidatat non proident, sunt in culpa qui officia deserunt mollit anim id est laborum.</p>
      <p>Lorem ipsum dolor sit amet, consectetur adipisicing elit, sed do eiusmod tempor incididunt ut labore et dolore magna aliqua. Ut enim ad minim veniam, quis nostrud exercitation ullamco laboris nisi ut aliquip ex ea commodo consequat. Duis aute irure dolor in reprehenderit in voluptate velit esse cillum dolore eu fugiat nulla pariatur. Excepteur sint occaecat cupidatat non proident, sunt in culpa qui officia deserunt mollit anim id est laborum.</p>
      <p>Lorem ipsum dolor sit amet, consectetur adipisicing elit, sed do eiusmod tempor incididunt ut labore et dolore magna aliqua. Ut enim ad minim veniam, quis nostrud exercitation ullamco laboris nisi ut aliquip ex ea commodo consequat. Duis aute irure dolor in reprehenderit in voluptate velit esse cillum dolore eu fugiat nulla pariatur. Excepteur sint occaecat cupidatat non proident, sunt in culpa qui officia deserunt mollit anim id est laborum.</p>
      <p>Lorem ipsum dolor sit amet, consectetur adipisicing elit, sed do eiusmod tempor incididunt ut labore et dolore magna aliqua. Ut enim ad minim veniam, quis nostrud exercitation ullamco laboris nisi ut aliquip ex ea commodo consequat. Duis aute irure dolor in reprehenderit.</p>
      <p class="closing">Yours Sincerely,</p>
      <div class="signature" role="img" aria-label="Handwritten signature of the sender"></div>
    </div>

    <address class="sender" style="font-style:normal">
      <strong>Harbor Vale LTD.</strong><br>
      48 Larchmont Crescent, Maple Ridge, ON L6K 3R2
    </address>

    <div class="footer-band"><span class="gold"></span><span class="navy"></span></div>
  </section>

  <div class="card card-light">
    <div class="brand"><span class="brand-dot"></span>Harbor Vale</div>
  </div>
  <div class="card card-dark">
    <div class="brand"><span class="brand-dot"></span>Harbor Vale</div>
  </div>
</body>
</html>
```